SaaS Early tech startup business card design

Unique design for experience ecommerce platform company. the business cards will be used by executive members. conformance with color code is required.

```html
<!DOCTYPE html>
<html lang="en">
<head>
<meta charset="utf-8">
<title>Nuvra business card</title>
<link href="https://fonts.googleapis.com/css2?family=Open+Sans:wght@400;600;700&family=Ubuntu:wght@500;700&display=swap" rel="stylesheet">
<style>
  :root {
    --backdrop: #1d1d1e;
    --brand-blue: #17668f;
    --deep-blue: #13608a;
    --brand-teal: #12b595;
    --soft-teal: #2cc0a2;
    --paper: #ffffff;
    --ink: #1f1f1f;
  }
  * { margin: 0; padding: 0; box-sizing: border-box; }
  html, body {
    width: 1200px; height: 988px; overflow: hidden;
    background: var(--backdrop);
  }
  .stage {
    position: relative; width: 1200px; height: 988px;
    display: flex; flex-direction: column; align-items: center;
    justify-content: center; gap: 60px;
  }
  .card {
    position: relative; width: 600px; height: 343px;
    border-radius: 22px; overflow: hidden;
  }
  .card-back {
    background: var(--brand-blue);
    display: flex; align-items: center; justify-content: center;
  }
  .wordmark {
    font-family: "Ubuntu", sans-serif; font-weight: 700;
    letter-spacing: -2px; line-height: 1;
  }
  .card-back .wordmark { font-size: 120px; color: var(--soft-teal); }
  .card-front { background: var(--paper); }
  .card-front .wordmark {
    position: absolute; left: 228px; top: 48px;
    font-size: 86px; color: var(--brand-blue);
  }
  .holder {
    position: absolute; left: 120px; top: 186px; text-align: right; width: 170px;
    font-family: "Open Sans", sans-serif;
  }
  .holder-name { font-weight: 700; font-size: 25px; color: var(--brand-blue); line-height: 1.1; }
  .holder-role { font-size: 14px; color: var(--ink); }
  .divider {
    position: absolute; left: 306px; top: 176px; width: 1.5px; height: 78px;
    background: var(--brand-teal);
  }
  .contacts {
    position: absolute; left: 322px; top: 176px; list-style: none;
    font-family: "Open Sans", sans-serif; font-size: 14px; color: var(--ink);
  }
  .contacts li { display: flex; align-items: center; gap: 8px; height: 26px; }
  .contacts svg { width: 12px; height: 12px; fill: var(--brand-blue); }
  .bands { position: absolute; left: 0; bottom: 30px; width: 600px; height: 40px; }
  .address {
    position: absolute; left: 196px; bottom: 39px;
    font-family: "Open Sans", sans-serif; font-size: 14px; color: var(--paper);
  }
</style>
</head>
<body>
<main class="stage">
  <section class="card card-back">
    <span class="wordmark">Nuvra</span>
  </section>

  <section class="card card-front">
    <span class="wordmark">Nuvra</span>

    <div class="holder">
      <p class="holder-name">Elin Varga</p>
      <p class="holder-role">Managing Director</p>
    </div>

    <div class="divider"></div>

    <ul class="contacts">
      <li>
        <svg viewBox="0 0 24 24"><path d="M6.6 10.8a15 15 0 0 0 6.6 6.6l2.2-2.2a1 1 0 0 1 1-.25 11.4 11.4 0 0 0 3.6.57 1 1 0 0 1 1 1V20a1 1 0 0 1-1 1A17 17 0 0 1 3 4a1 1 0 0 1 1-1h3.5a1 1 0 0 1 1 1c0 1.25.2 2.45.57 3.57a1 1 0 0 1-.25 1z"/></svg>
        +000 555 0142
      </li>
      <li>
        <svg viewBox="0 0 24 24"><path d="M2 5h20v14H2z M2 5l10 8 10-8" fill="none" stroke="#17668f" stroke-width="2.4"/></svg>
        hello@nuvramail.com
      </li>
      <li>
        <svg viewBox="0 0 24 24"><circle cx="12" cy="12" r="9" fill="none" stroke="#17668f" stroke-width="2.4"/><path d="M3 12h18M12 3c3 3 3 15 0 18M12 3c-3 3-3 15 0 18" fill="none" stroke="#17668f" stroke-width="1.6"/></svg>
        www.nuvraplatform.com
      </li>
    </ul>

    <svg class="bands" viewBox="0 0 600 40" aria-hidden="true">
      <polygon points="0,8 178,8 170,40 0,40" fill="var(--brand-teal)"/>
      <polygon points="186,8 508,8 500,40 178,40" fill="var(--deep-blue)"/>
      <polygon points="516,0 600,0 600,26 510,26" fill="var(--brand-teal)"/>
    </svg>
    <p class="address">18 Harbor Lane, Westfield, Country - 40217</p>
  </section>
</main>
</body>
</html>
```